Reputable business cards for Diplom Kauffrau, Privat und Geschäftslich

The business cards should be reputable, valuable and elegant in order to be able to use them for business. The design should also include a sophistication that is conspicuous. This could be a picture, an ornament, a sublime print or a kind of logo of the initials of my name "MD". The font should be clear and legible.
Target Market(s)
Business contacts, friends and acquaintances
Contact Information for Business Card
Diplom-Kauffrau Mirela Donat
Lindenhofweg 7 50931 Kerpen
Mobil +49 171 804 29 57
e-mail mirela.donat@postwerk.de
Colors
Designer to choose colors to be used in the design.
Requirements
Must have
- Clear and easy to read font My name in larger font than the other information Visual conspicuity / specificity
Nice to have
- Different colors
Should not have
- Ornate font, playful

```html
<!DOCTYPE html>
<html lang="de">
<head>
<meta charset="utf-8">
<title>Mirela Donat – Visitenkarte</title>
<link rel="stylesheet" href="https://fonts.googleapis.com/css2?family=Montserrat:wght@500&family=Roboto:wght@500&family=Work+Sans:wght@400&display=swap">
<style>
  :root {
    --stage: #2b2b2c;
    --paper: #ffffff;
    --charcoal: #414143;
    --ink: #3a3a3c;
    --brand-blue: #1077c0;
    --white: #ffffff;
  }
  * { box-sizing: border-box; margin: 0; padding: 0; }
  html, body {
    width: 1200px; height: 900px; overflow: hidden;
    background: var(--stage);
  }
  .stage { position: relative; width: 1200px; height: 900px; }

  .card {
    position: absolute; left: 261px; width: 656px; height: 358px;
  }
  .card--front { top: 69px; background: var(--paper); }
  .card--back { top: 472px; background: var(--charcoal); }

  .wordmark {
    position: absolute; display: flex; align-items: center; gap: 10px;
    font-family: "Montserrat", sans-serif; font-weight: 500;
    letter-spacing: 0.02em; white-space: nowrap;
  }
  .wordmark__square { display: block; background: var(--brand-blue); }

  .card--front .wordmark { left: 28px; top: 92px; font-size: 25px; color: var(--ink); }
  .card--front .wordmark__square { width: 18px; height: 18px; }

  .holder {
    position: absolute; right: 30px; top: 210px; text-align: right;
  }
  .holder__name {
    font-family: "Roboto", sans-serif; font-weight: 500;
    font-size: 26px; line-height: 1; color: var(--brand-blue); letter-spacing: 0.01em;
  }
  .holder__title {
    margin-top: 6px;
    font-family: "Work Sans", sans-serif; font-size: 15.5px; color: var(--ink); letter-spacing: 0.04em;
  }
  .edge-tab {
    position: absolute; right: 0; top: 215px; width: 12px; height: 37px; background: var(--brand-blue);
  }
  .divider {
    position: absolute; left: 28px; right: 30px; top: 269px; height: 2px; background: var(--brand-blue);
  }

  .contact, .address {
    position: absolute; top: 293px;
    font-family: "Work Sans", sans-serif; font-size: 15.5px; line-height: 21px;
    color: var(--ink); letter-spacing: 0.05em;
  }
  .contact { left: 28px; }
  .contact__row { display: flex; align-items: center; gap: 8px; }
  .contact__icon { width: 11px; height: 11px; flex: none; }
  .address { right: 30px; text-align: right; }

  .card--back .wordmark {
    left: 0; right: 0; justify-content: center; top: 226px;
    font-size: 41px; color: var(--white); gap: 16px;
  }
  .card--back .wordmark__square { width: 30px; height: 30px; }
</style>
</head>
<body>
<main class="stage">
  <section class="card card--front" aria-label="Visitenkarte Vorderseite">
    <div class="wordmark">
      <span class="wordmark__square"></span>
      <span class="wordmark__name">MIRELA DONAT</span>
    </div>

    <div class="holder">
      <p class="holder__name">MIRELA DONAT</p>
      <p class="holder__title">Diplom-Kauffrau</p>
    </div>
    <span class="edge-tab"></span>
    <span class="divider"></span>

    <div class="contact">
      <p class="contact__row">
        <svg class="contact__icon" viewBox="0 0 12 12" aria-hidden="true">
          <path d="M3 1 L4.6 3.6 L3.6 4.6 Q4.6 7.2 7.4 8.4 L8.4 7.4 L11 9 L10 11 Q3.5 10.5 1 2 Z" fill="none" stroke="#1077c0" stroke-width="1.2" stroke-linejoin="round"/>
        </svg>
        <span>+49 171 804 29 57</span>
      </p>
      <p class="contact__row">
        <svg class="contact__icon" viewBox="0 0 12 12" aria-hidden="true">
          <rect x="0.8" y="2.3" width="10.4" height="7.4" rx="1" fill="none" stroke="#1077c0" stroke-width="1.2"/>
          <path d="M1 3 L6 6.6 L11 3" fill="none" stroke="#1077c0" stroke-width="1.2"/>
        </svg>
        <span>mirela.donat@postwerk.de</span>
      </p>
    </div>

    <div class="address">
      <p>Lindenhofweg</p>
      <p>7 50931 Kerpen</p>
    </div>
  </section>

  <section class="card card--back" aria-label="Visitenkarte Rückseite">
    <div class="wordmark">
      <span class="wordmark__square"></span>
      <span class="wordmark__name">MIRELA DONAT</span>
    </div>
  </section>
</main>
</body>
</html>
```